Esthetically Pleasing Core Values and Brand Promise for Accounting Firm

I would like a cohesive design that ties together my core values and brand promise. My firm, Maple Finch Advisory, provides accounting work to small businesses. I prefer modern and clean designs. I want my Core Values and Brand Promise to represent me - sole entrepreneur, married, mother of two kids, modern esthetics, clean lines, organized, colorful (teals, greys, white, yellows)

Industry/Entity Type

Public Accounting

Colors
33b8a4

```html
<!DOCTYPE html>
<html lang="en">
<head>
<meta charset="utf-8">
<title>Maple Finch Advisory – Core Values and Brand Promise</title>
<link href="https://fonts.googleapis.com/css2?family=Federo&display=swap" rel="stylesheet">
<style>
  :root {
    --teal-light: #8fd3d6;
    --teal: #5fb9c0;
    --teal-deep: #3e9fa8;
    --wood-dark: #4a3424;
    --wood: #7a5a40;
    --wood-light: #a68463;
    --paper: #d9dcdc;
    --white: #ffffff;
  }
  * { margin: 0; padding: 0; box-sizing: border-box; }
  html, body {
    width: 851px;
    height: 1200px;
    overflow: hidden;
    background: var(--white);
  }
  .poster {
    position: relative;
    width: 851px;
    height: 1200px;
    overflow: hidden;
    font-family: "Federo", "Trebuchet MS", sans-serif;
    color: var(--white);
    text-transform: uppercase;
  }
  .band { position: absolute; left: 0; width: 851px; }
  .band-masthead {
    top: 0; height: 314px;
    background:
      radial-gradient(ellipse at 20% 40%, rgba(255,255,255,0.25), transparent 55%),
      linear-gradient(135deg, var(--teal-light) 0%, var(--teal) 55%, var(--teal-deep) 100%);
  }
  .band-values {
    top: 314px; height: 472px;
    background:
      radial-gradient(ellipse at 75% 25%, rgba(230,230,230,0.55), transparent 45%),
      radial-gradient(ellipse at 85% 75%, rgba(235,235,235,0.5), transparent 35%),
      linear-gradient(160deg, var(--wood-light) 0%, var(--wood) 45%, var(--wood-dark) 100%);
  }
  .band-promise {
    top: 786px; height: 414px;
    background:
      radial-gradient(ellipse at 60% 45%, rgba(255,255,255,0.28), transparent 60%),
      linear-gradient(170deg, var(--teal) 0%, var(--teal-light) 50%, var(--teal) 100%);
  }
  .wordmark {
    position: absolute;
    top: 44px; left: 0; width: 851px;
    text-align: center;
    font-weight: 400;
    line-height: 1;
    color: var(--white);
  }
  .wordmark-line {
    display: block;
    font-size: 76px;
    letter-spacing: 4px;
    margin-bottom: 8px;
  }
  .wordmark-sub {
    display: block;
    font-size: 38px;
    letter-spacing: 5px;
    margin-top: 18px;
  }
  .section-title {
    position: absolute;
    left: 30px;
    font-size: 30px;
    font-weight: 400;
    line-height: 41px;
    text-decoration: underline;
    text-decoration-thickness: 1px;
    text-underline-offset: 5px;
    white-space: nowrap;
  }
  .values-title { top: 334px; }
  .promise-title { top: 806px; left: 32px; }
  .statement-list {
    position: absolute;
    list-style: none;
    font-size: 26px;
    line-height: 37.7px;
    white-space: nowrap;
  }
  .values-list {
    top: 388px; left: 29px;
    text-shadow: 0 1px 3px rgba(0,0,0,0.45);
  }
  .promise-list { top: 909px; left: 33px; }
  .statement-list span { display: block; }
</style>
</head>
<body>
<main class="poster">
  <section class="band band-masthead" role="img" aria-label="Soft teal-toned photo of a desk with a pen and paperwork"></section>
  <section class="band band-values" role="img" aria-label="Photo of a business handshake over a wooden desk with a laptop and financial reports"></section>
  <section class="band band-promise" role="img" aria-label="Soft teal-toned photo of a calculator on a desk"></section>

  <h1 class="wordmark">
    <span class="wordmark-line">MAPLE</span>
    <span class="wordmark-line">FINCH</span>
    <span class="wordmark-sub">ADVISORY</span>
  </h1>

  <h2 class="section-title values-title">Maple Finch Advisory</h2>
  <ul class="statement-list values-list">
    <li><span>• Empower – We are dedicated, appreciative</span><span>and respectful of people’s time and purpose.</span></li>
    <li><span>• Client focused – We provide a personal</span><span>service that goes above the standards of</span><span>professional care.</span></li>
    <li><span>• Rectitude – We know the difference</span><span>between what we have the right to do and</span><span>what the right thing to do is.</span></li>
    <li><span>• Relentless – We believe that the longer we</span><span>try to do our best, the better we become.</span></li>
  </ul>

  <h2 class="section-title promise-title">Brand promise – Trust, transparency and<br>dependability</h2>
  <ul class="statement-list promise-list">
    <li><span>• Tax - Maple Finch provides all clients with a</span><span>trusted tax advisor who provides accuracy in</span><span>all filings and ensures your compliance with</span><span>all government agencies.</span></li>
    <li><span>• Accounting - Maple Finch provides all business</span><span>owners with the financial visibility needed to</span><span>foster growth and facilitate goals.</span></li>
  </ul>
</main>
</body>
</html>
```